Sunny Paths and joy Business card

I have a logo, but will like a business card design. Is for a travel agency in Mexico. We focus in family experiences.

I will liek some thing different and unique, from the traditional business card, something to get remmeber for.

Business card information:

Leandro T. Ocampo
leandro@sunnypathsjoy.example

Alameda 482, 3 piso
Col. Tlalpizco
Mexico, D.F. 07320

office: (55) 5000-0142
mobile: (55) 9000-0187

www.sunnypathsjoy.example
@sunnypjoy
blog: sunnypathsandjoy.blogsite.example
facebook: SunnyPathsAndJoy

```html
<!DOCTYPE html>
<html lang="en">
<head>
<meta charset="utf-8">
<title>Sunny Paths and joy – Business Card</title>
<link href="https://fonts.googleapis.com/css2?family=Arimo:wght@400;700&display=swap" rel="stylesheet">
<style>
  :root {
    --page-bg: #e9ecef;
    --card-white: #ffffff;
    --blue-deep: #1f4f9e;
    --blue-deep-end: #2c62b6;
    --blue-band: #2a7bc8;
    --blue-band-end: #3488d2;
    --blue-name: #1c3c86;
    --blue-light: #4a8fd8;
    --text-on-blue: #ffffff;
  }
  * { box-sizing: border-box; margin: 0; padding: 0; }
  html, body {
    width: 1200px; height: 900px; overflow: hidden;
    background: var(--page-bg);
    font-family: "Arimo", Arial, sans-serif;
  }
  .card {
    position: absolute; left: 100px; top: 164px;
    width: 1000px; height: 572px;
    background: var(--card-white);
    box-shadow: 0 10px 30px rgba(0,0,0,0.18);
    overflow: hidden;
  }
  .top-rule {
    position: absolute; left: 300px; right: 0; top: 0; height: 7px;
    background: var(--blue-band);
  }
  .brand {
    position: absolute; left: 40px; top: 92px;
    display: flex; align-items: center; gap: 14px;
    color: var(--blue-deep);
    font-weight: 700; font-size: 30px; line-height: 1;
  }
  .brand-dot {
    width: 34px; height: 34px; border-radius: 50%;
    background: var(--blue-band); flex: none;
  }
  .identity {
    position: absolute; right: 36px; top: 40px; text-align: right;
  }
  .identity .person {
    color: var(--blue-name); font-weight: 700; font-size: 34px; line-height: 40px;
  }
  .identity .email {
    color: var(--blue-light); font-size: 24px; line-height: 30px;
  }
  .band-left {
    position: absolute; left: 0; top: 240px; width: 380px; height: 92px;
    background: linear-gradient(90deg, var(--blue-deep), var(--blue-deep-end));
  }
  .band-right {
    position: absolute; left: 384px; right: 0; top: 240px; height: 206px;
    background: linear-gradient(90deg, var(--blue-band), var(--blue-band-end));
    padding: 20px 0 0 22px;
    color: var(--text-on-blue); font-size: 25px; line-height: 30px;
  }
  .band-divider {
    position: absolute; left: 380px; top: 240px; width: 4px; height: 206px;
    background: var(--card-white);
  }
  .band-right .phones { margin-top: 22px; }
  .social {
    position: absolute; left: 406px; top: 462px;
    color: var(--blue-light); font-size: 22px; line-height: 28px;
  }
</style>
</head>
<body>
  <article class="card">
    <div class="top-rule"></div>

    <div class="brand">
      <span class="brand-dot"></span>
      <span class="brand-name">Sunny Paths and joy</span>
    </div>

    <header class="identity">
      <div class="person">Leandro T. Ocampo</div>
      <div class="email">leandro@sunnypathsjoy.example</div>
    </header>

    <div class="band-left"></div>
    <div class="band-divider"></div>
    <section class="band-right">
      <address class="postal" style="font-style:normal">
        <div>Alameda 482, 3 piso, Col. Tlalpizco</div>
        <div>Mexico, D.F. 07320</div>
      </address>
      <div class="phones">
        <div>office: (55) 5000-0142</div>
        <div>mobile: (55) 9000-0187</div>
      </div>
    </section>

    <section class="social">
      <div>@sunnypjoy</div>
      <div>blog: sunnypathsandjoy.blogsite.example</div>
      <div>facebook: SunnyPathsAndJoy</div>
    </section>
  </article>
</body>
</html>
```